Homepage Redesign - Hi-tech business Law Firm

I'm looking for an updated graphic design (pdf file) for the homepage of dorvantlegal.ca (and which will form the general template of the other pages - but you don't need to design that). Detailed specs are in the Word file.

Deliverable is 1 pdf file that I find good looking, that sets forth the layout of the new page.

Target Market(s)

Sophisticated customers

Industry/Entity Type

Legal

Number of Pages Required

1 page

Requirements
Nice to have
• For a main background, tech type images to do with high powered boardrooms, computers, graphs, numbers, high tech manufacturing lines etc. Also, I tend to like blues and light greys, and uploaded a file today that shows my generally preferred layout, which a few of you have been getting close to.
Should not have
• Any mention of 'Personal Injury,' backgrounds that include books, or buildings with roman columns. Page should not be in dark colors or harsh on the eyes.

```html
<!DOCTYPE html>
<html lang="en">
<head>
<meta charset="utf-8">
<title>Dorvant Legal — Home</title>
<link href="https://fonts.googleapis.com/css2?family=PT+Serif:wght@400;700&family=Poppins:wght@300;400;500;600&display=swap" rel="stylesheet">
<style>
:root{
  --navy:#0d4466;
  --navy-dark:#0a3350;
  --yellow:#f5c518;
  --red:#d6202b;
  --grey-bg:#f4f5f7;
  --text:#222;
  --muted:#7a7f87;
  --line:#e3e6ea;
  --white:#fff;
}
*{box-sizing:border-box;margin:0;padding:0}
html,body{width:1200px;height:5373px;overflow:hidden}
body{font-family:"Poppins",sans-serif;color:var(--text);background:var(--white);position:relative}
.abs{position:absolute}
.btn-outline{border:1.5px solid var(--navy);color:var(--navy);font-family:"PT Serif",serif;font-weight:700;display:inline-flex;align-items:center;gap:10px;border-radius:2px;background:#fff}

/* header */
.topbar{left:600px;top:0;width:600px;height:25px;background:var(--navy);clip-path:polygon(20px 0,100% 0,100% 100%,0 100%);color:#fff;font-size:8px;display:flex;align-items:center;justify-content:flex-end;gap:40px;padding-right:85px}
.brand{left:83px;top:34px;display:flex;align-items:center;gap:12px}
.brand-mark{width:14px;height:14px;background:var(--navy)}
.brand-name{font-family:"PT Serif",serif;font-weight:400;font-size:22px;letter-spacing:4px;color:var(--navy);white-space:nowrap}
.nav{left:372px;top:54px;display:flex;gap:48px;font-family:"PT Serif",serif;font-size:13px;color:#333}
.nav .active{color:var(--navy);border-bottom:1px solid var(--navy)}
.nav-icons{left:870px;top:50px;display:flex;gap:18px}
.cta-eval{left:958px;top:40px;width:159px;height:40px;justify-content:center;font-size:13px;font-weight:400}

/* hero */
.hero{left:0;top:98px;width:1200px;height:622px;background:linear-gradient(100deg,#6d8fae 0%,#8aa8c4 35%,#a9bfd3 55%,#5f7f9e 100%)}
.hero-portrait{left:640px;top:98px;width:420px;height:470px;background:linear-gradient(180deg,#a3b4c3 0%,#5a6f84 60%,#2f3f52 100%);border-radius:200px 200px 0 0}
.hero-title{left:83px;top:198px;font-family:"PT Serif",serif;color:#fff;font-size:40px;line-height:50px;font-weight:700}
.hero-copy{left:83px;top:400px;color:#fff;font-size:11px;line-height:17px;font-family:"PT Serif",serif}
.hero-btn{top:492px;height:38px;padding:0 18px;color:#fff;font-family:"PT Serif",serif;font-weight:700;font-size:14px;display:flex;align-items:center;gap:10px}
.hero-btn.read{left:83px;background:var(--navy)}
.hero-btn.video{left:258px;background:var(--red)}

/* intro */
.consult{left:83px;top:803px;width:420px;height:537px;background:#fff;box-shadow:0 4px 24px rgba(0,0,0,.08);border-radius:6px;padding:48px 18px 0}
.consult h3{text-align:center;color:var(--navy);font-size:19px;font-weight:600;line-height:30px;margin-bottom:26px}
.field-row{display:flex;gap:16px;margin-bottom:18px}
.field{flex:1;height:48px;background:#f1f2f4;border-radius:3px;font-size:10px;color:#9aa0a8;padding:16px 12px}
.field.area{height:112px;flex:none;width:100%}
.consent{font-size:7.5px;color:var(--muted);line-height:11px;margin-bottom:40px;width:320px}
.send{display:block;margin:0 auto;width:170px;height:36px;background:var(--yellow);color:#fff;font-size:15px;text-align:center;line-height:36px;border-radius:3px}
.intro-text{left:608px;top:843px;width:509px}
.intro-text h2{font-family:"PT Serif",serif;font-size:18px;line-height:32px;color:var(--navy-dark);margin-bottom:28px}
.intro-text p{font-size:12px;line-height:24px;color:var(--muted);margin-bottom:24px}
.intro-text .btn-outline{height:36px;padding:0 16px;font-size:14px}

/* practices */
.practices{left:0;top:1505px;width:1200px;height:635px;background:var(--grey-bg)}
.sec-title{font-family:"PT Serif",serif;font-weight:700;color:var(--navy);font-size:30px}
.view-all{left:958px;top:1580px;width:159px;height:40px;justify-content:center;font-size:15px}
.card{top:1648px;width:335px;height:402px;background:#fff;box-shadow:0 2px 12px rgba(0,0,0,.06)}
.card-media{height:208px}
.card-icon{position:absolute;right:40px;top:174px;width:68px;height:68px;border-radius:50%;background:var(--yellow);display:flex;align-items:center;justify-content:center}
.card h4{margin:38px 20px 10px;font-size:19px;font-weight:500;color:#222}
.card p{margin:0 20px 18px;font-size:10px;line-height:15px;color:var(--muted)}
.card .mini{margin-left:20px;height:26px;padding:0 12px;border:1.5px solid var(--navy);border-radius:14px;font-size:10px;color:var(--navy);display:inline-flex;align-items:center;gap:8px;font-weight:500}
.dots{left:535px;top:2090px;display:flex;gap:18px}
.dots span{width:32px;height:3px;background:#ccc}
.dots span:first-child{background:#222}

/* stats */
.stats{left:108px;top:2275px;width:984px;height:325px;background:#fff;box-shadow:0 6px 28px rgba(0,0,0,.1);border-radius:6px;display:flex}
.stat{width:246px;border-right:1px solid var(--line);text-align:center;padding-top:68px}
.stat .num{font-size:38px;font-weight:500;margin-top:30px}
.stat .lbl{font-size:15px;color:var(--muted);margin-top:22px}
.stat-panel{flex:1;background:var(--navy);border-radius:6px;color:#fff;padding:58px 22px 0}
.stat-panel h4{font-size:26px;font-weight:500;margin-bottom:18px}
.stat-panel p{font-size:11px;line-height:18px;margin-bottom:44px}
.signup{display:inline-block;background:#fff;color:var(--navy);font-weight:600;font-size:15px;padding:9px 38px;border-radius:22px}

/* recognition */
.recog{left:0;top:2715px;width:1200px;height:275px;background:var(--grey-bg)}
.badge{left:310px;top:2858px;width:208px;height:54px;background:linear-gradient(90deg,var(--red) 0 65%,#1b1b1b 65%);border-radius:4px}
.recog-text{left:570px;top:2852px;width:320px;font-size:11px;line-height:17px;color:var(--muted)}

/* lawyers */
.lawyer{top:3225px;width:160px;text-align:center}
.lawyer .photo{height:208px;border-radius:10px}
.lawyer h5{font-size:16px;font-weight:600;margin-top:22px}
.lawyer span{font-size:12px;color:var(--navy)}

/* testimonials */
.testi{left:0;top:3590px;width:1200px;height:550px;background:var(--grey-bg)}
.testi-card{left:258px;top:3755px;width:684px;height:310px;background:#fff;text-align:center;padding-top:40px}
.testi-card p{font-size:16px;line-height:28px;color:#555;margin:26px 0 30px}
.testi-card h6{font-size:15px;font-weight:600}
.testi-card small{font-size:8px;color:#aaa}
.arrow{width:38px;height:38px;border-radius:50%;display:flex;align-items:center;justify-content:center;top:3890px}

/* news */
.news-main{left:83px;top:4333px;width:509px;height:387px;background:#fff;box-shadow:0 2px 14px rgba(0,0,0,.07);border-bottom:2px solid var(--navy)}
.news-main .media{height:220px}
.news-main .body{padding:14px 28px}
.date{font-size:9px;color:#333}
.news-main h4{font-size:16px;font-weight:500;margin:12px 0 12px}
.news-main p{font-size:9.5px;line-height:14px;color:var(--muted);margin-bottom:16px;width:400px}
.news-main a{font-size:10px;color:var(--navy);font-weight:600;border-bottom:2px solid var(--navy);text-decoration:none}
.news-item{left:608px;width:509px;height:122px;display:flex;background:#fff;border-bottom:2px solid var(--navy);box-shadow:0 2px 14px rgba(0,0,0,.06)}
.news-item .media{width:160px;height:120px}
.news-item .body{padding:18px 14px}
.news-item h5{font-size:19px;font-weight:400;line-height:29px;color:#444;margin-bottom:16px}

/* footer */
.footer{left:0;top:4890px;width:1200px;height:483px;background:var(--navy-dark);color:#fff}
.f-col h6{font-family:"PT Serif",serif;font-size:18px;font-weight:700;margin-bottom:26px}
.f-col li{list-style:none;font-family:"PT Serif",serif;font-size:12px;margin-bottom:22px}
.f-contact{display:flex;gap:12px;font-family:"PT Serif",serif;font-size:12px;line-height:16px;margin-bottom:22px}
.f-bottom{font-size:11px}
</style>
</head>
<body>

<!-- header -->
<div class="abs topbar"><span>GTA · Hamilton · Niagara</span><span>contact@dorvantlegal.ca</span><span>Call Us &nbsp;647 555 0142</span></div>
<div class="abs brand"><span class="brand-mark"></span><span class="brand-name">DORVANT LEGAL</span></div>
<nav class="abs nav"><span class="active">Pratice Areas</span><span>About</span><span>News</span><span>Resources</span><span>Contact Us</span></nav>
<div class="abs nav-icons">
  <svg width="16" height="16" viewBox="0 0 16 16"><circle cx="6.5" cy="6.5" r="5" fill="none" stroke="#0d4466" stroke-width="2"/><path d="M10 10l5 5" stroke="#0d4466" stroke-width="2"/></svg>
  <svg width="26" height="16" viewBox="0 0 26 16"><circle cx="8" cy="5" r="4" fill="#0d4466"/><path d="M1 16c0-5 14-5 14 0z" fill="#0d4466"/><path d="M19 7l3 3 3-3z" fill="#0d4466"/></svg>
</div>
<div class="abs btn-outline cta-eval">Free Case Evaluation</div>

<!-- hero -->
<div class="abs hero" role="img" aria-label="Blue-toned photo backdrop of a modern office"></div>
<div class="abs hero-portrait" role="img" aria-label="Portrait of the lead lawyer in a suit and tie"></div>
<svg class="abs" style="left:0;top:560px" width="1200" height="170" viewBox="0 0 1200 170">
  <polygon points="300,130 1200,10 1200,45 300,150" fill="#f5c518"/>
  <polygon points="0,160 1200,40 1200,170 0,170" fill="#fff"/>
</svg>
<h1 class="abs hero-title">Winning.<br>My Client Depend On Me For It.<br>Why Shouldn’t You ?</h1>
<p class="abs hero-copy">Lorem Ipsum is simply dummy text of the printing and typesetting industry.<br>Lorem Ipsum has been the industry’s standard dummy text</p>
<div class="abs hero-btn read"><svg width="14" height="14" viewBox="0 0 14 14"><rect x="2" y="1" width="10" height="12" fill="none" stroke="#fff" stroke-width="1.5"/><path d="M5 1v12" stroke="#fff" stroke-width="1.5"/></svg>Read More</div>
<div class="abs hero-btn video"><svg width="12" height="10" viewBox="0 0 12 10"><rect width="12" height="10" rx="2" fill="#fff"/><path d="M5 3l3 2-3 2z" fill="#d6202b"/></svg>Video Library</div>

<!-- intro -->
<div class="abs consult">
  <h3>Schedule your initial consult<br>with our lawyers.</h3>
  <div class="field-row"><div class="field">First Name</div><div class="field">Last Name</div></div>
  <div class="field-row"><div class="field">Email</div><div class="field">Phone</div></div>
  <div class="field-row"><div class="field area">Case Details</div></div>
  <p class="consent">*By using this site and or submitting this form, I agree to the Privacy Policy and Terms of Use.</p>
  <div class="send">Send</div>
</div>
<div class="abs intro-text">
  <h2>Your Experienced Toronto And Hamilton Lawyers – Getting The Results That Matter</h2>
  <p>Dorvant Legal is a boutique litigation firm with law offices in Toronto and Hamilton. We concentrate our legal practice on complex business litigation, professional negligence (malpractice) claims, technology contracts, and insurance coverage disputes. We take an innovative approach to our client’s legal problems, and are guided by the philosophy that our job is to get results.</p>
  <p>The lawyers at Dorvant Legal have the reputation for vigorously representing their clients’ interests and competing hard to obtain the best possible results. With experience at all stages of legal disputes, the lawyers at Dorvant Legal are equally at home negotiating in a boardroom or presenting a case at trial. We hope that you take the time to explore our website to find out how our record of excellence, expertise and many years of experience can assist you.</p>
  <div class="btn-outline">Read More <svg width="26" height="8" viewBox="0 0 26 8"><path d="M0 4h24M20 1l4 3-4 3" stroke="#0d4466" fill="none" stroke-width="1.5"/></svg></div>
</div>

<!-- practices -->
<div class="abs practices"></div>
<h2 class="abs sec-title" style="left:83px;top:1575px">Area of Practices</h2>
<div class="abs btn-outline view-all">View All <svg width="26" height="8" viewBox="0 0 26 8"><path d="M0 4h24M20 1l4 3-4 3" stroke="#0d4466" fill="none" stroke-width="1.5"/></svg></div>

<div class="abs card" style="left:83px">
  <div class="card-media" role="img" aria-label="Hand signing a contract" style="background:linear-gradient(135deg,#d8b895,#efe7dc 55%,#b89777)"></div>
  <div class="card-icon"><svg width="30" height="28" viewBox="0 0 30 28"><path d="M15 2L2 9h26z" fill="#fff"/><path d="M6 11v11M12 11v11M18 11v11M24 11v11M3 25h24" stroke="#fff" stroke-width="2.5"/></svg></div>
  <h4>Business Litigation</h4>
  <p>Lorem Ipsum is simply dummy text of the typesetting industry.Lorem Ipsum is simply dummy text of the typesetting industry.</p>
  <span class="mini">View More <svg width="14" height="8" viewBox="0 0 14 8"><path d="M0 4h12M9 1l3 3-3 3" stroke="#0d4466" fill="none" stroke-width="1.5"/></svg></span>
</div>
<div class="abs card" style="left:433px">
  <div class="card-media" role="img" aria-label="Laptop showing financial charts" style="background:linear-gradient(135deg,#5c6670,#c9ced3 50%,#3f474f)"></div>
  <div class="card-icon"><svg width="28" height="28" viewBox="0 0 28 28"><rect x="4" y="4" width="10" height="6" transform="rotate(45 9 7)" fill="#fff"/><path d="M12 14l10 10" stroke="#fff" stroke-width="3"/><path d="M2 26h14" stroke="#fff" stroke-width="3"/></svg></div>
  <h4>Professional Negligence</h4>
  <p>Lorem Ipsum is simply dummy text of the typesetting industry.Lorem Ipsum is simply dummy text of the typesetting industry.</p>
  <span class="mini">View More <svg width="14" height="8" viewBox="0 0 14 8"><path d="M0 4h12M9 1l3 3-3 3" stroke="#0d4466" fill="none" stroke-width="1.5"/></svg></span>
</div>
<div class="abs card" style="left:783px">
  <div class="card-media" role="img" aria-label="Policy documents and charts on a boardroom table" style="background:linear-gradient(135deg,#b7c9d8,#e3e8ee 50%,#8eaac2)"></div>
  <div class="card-icon"><svg width="26" height="30" viewBox="0 0 26 30"><path d="M13 2l10 4v8c0 7-5 12-10 14C8 26 3 21 3 14V6z" fill="none" stroke="#fff" stroke-width="2.5"/><path d="M8 15l4 4 6-7" fill="none" stroke="#fff" stroke-width="2.5"/></svg></div>
  <h4>Insurance Coverage</h4>
  <p>Lorem Ipsum is simply dummy text of the typesetting industry.Lorem Ipsum is simply dummy text of the typesetting industry.</p>
  <span class="mini">View More <svg width="14" height="8" viewBox="0 0 14 8"><path d="M0 4h12M9 1l3 3-3 3" stroke="#0d4466" fill="none" stroke-width="1.5"/></svg></span>
</div>
<div class="abs dots"><span></span><span></span><span></span></div>

<!-- stats -->
<div class="abs stats">
  <div class="stat"><svg width="62" height="62" viewBox="0 0 62 62"><path d="M31 4l7 5 9 0 3 8 7 6-3 8 3 8-7 6-3 8-9 0-7 5-7-5-9 0-3-8-7-6 3-8-3-8 7-6 3-8 9 0z" fill="none" stroke="#2b7ba8" stroke-width="2.5"/><path d="M20 31l8 8 15-16" fill="none" stroke="#2b7ba8" stroke-width="3"/></svg><div class="num">17+</div><div class="lbl">Years of Ligitation</div></div>
  <div class="stat"><svg width="62" height="62" viewBox="0 0 62 62"><path d="M31 4l7 5 9 0 3 8 7 6-3 8 3 8-7 6-3 8-9 0-7 5-7-5-9 0-3-8-7-6 3-8-3-8 7-6 3-8 9 0z" fill="none" stroke="#2b7ba8" stroke-width="2.5"/><path d="M20 31l8 8 15-16" fill="none" stroke="#2b7ba8" stroke-width="3"/></svg><div class="num">900+</div><div class="lbl">Cases Won</div></div>
  <div class="stat"><svg width="62" height="62" viewBox="0 0 62 62"><path d="M31 4l7 5 9 0 3 8 7 6-3 8 3 8-7 6-3 8-9 0-7 5-7-5-9 0-3-8-7-6 3-8-3-8 7-6 3-8 9 0z" fill="none" stroke="#2b7ba8" stroke-width="2.5"/><path d="M20 31l8 8 15-16" fill="none" stroke="#2b7ba8" stroke-width="3"/></svg><div class="num">840+</div><div class="lbl">Happy Clients</div></div>
  <div class="stat-panel">
    <h4>Lorem Ipsum</h4>
    <p>Lorem Ipsum is simply dummy text of the typesetting industry.Lorem Ipsum is simply dummy text of the typesetting industry.</p>
    <span class="signup">Sign Up</span>
  </div>
</div>

<!-- recognition -->
<div class="abs recog"></div>
<h2 class="abs sec-title" style="left:0;width:1200px;text-align:center;top:2748px">Our Recognization</h2>
<div class="abs badge" role="img" aria-label="Peer review rating badge"></div>
<p class="abs recog-text">An excellent rating for a lawyer with some experience. This rating indicates the attorney is widely respected by their peers for high professional achievement and ethical standards.</p>

<!-- lawyers -->
<h2 class="abs sec-title" style="left:0;width:1200px;text-align:center;top:3128px">Our Lawyers</h2>
<div class="abs lawyer" style="left:124px"><div class="photo" role="img" aria-label="Lawyer headshot" style="background:linear-gradient(180deg,#dfe3e6,#8a6d58)"></div><h5>John Smith</h5><span>Lawyer</span></div>
<div class="abs lawyer" style="left:387px"><div class="photo" role="img" aria-label="Lawyer headshot" style="background:linear-gradient(180deg,#7c6a5a,#4b4f5a)"></div><h5>John Smith</h5><span>Lawyer</span></div>
<div class="abs lawyer" style="left:650px"><div class="photo" role="img" aria-label="Lawyer headshot" style="background:linear-gradient(180deg,#9a3a2c,#2a2a2a)"></div><h5>John Smith</h5><span>Lawyer</span></div>
<div class="abs lawyer" style="left:913px"><div class="photo" role="img" aria-label="Lawyer headshot" style="background:linear-gradient(180deg,#a9c0d0,#4d6a86)"></div><h5>John Smith</h5><span>Lawyer</span></div>

<!-- testimonials -->
<div class="abs testi"></div>
<h2 class="abs sec-title" style="left:0;width:1200px;text-align:center;top:3680px">What Our Client Saying</h2>
<div class="abs testi-card">
  <svg width="150" height="26" viewBox="0 0 150 26"><g fill="#f5c518"><path id="st" d="M13 1l3.5 8 8.5.8-6.5 5.6 2 8.4L13 19.5 5.5 23.8l2-8.4L1 9.8 9.5 9z"/><use href="#st" x="31"/><use href="#st" x="62"/><use href="#st" x="93"/><use href="#st" x="124"/></g></svg>
  <p>Lorem Ipsum is simply dummy text<br>of the typesetting industry.Lorem<br>Ipsum is simply dummy text<br>of the typesetting industry.</p>
  <h6>John Smith</h6><small>Manager</small>
</div>
<div class="abs arrow" style="left:170px;background:#fff;box-shadow:0 2px 8px rgba(0,0,0,.1)"><svg width="14" height="10" viewBox="0 0 14 10"><path d="M13 5H2M5 1L1 5l4 4" stroke="#222" fill="none" stroke-width="1.5"/></svg></div>
<div class="abs arrow" style="left:992px;background:var(--navy)"><svg width="14" height="10" viewBox="0 0 14 10"><path d="M1 5h11M9 1l4 4-4 4" stroke="#fff" fill="none" stroke-width="1.5"/></svg></div>

<!-- news -->
<h2 class="abs sec-title" style="left:0;width:1200px;text-align:center;top:4245px">Latest News</h2>
<div class="abs news-main">
  <div class="media" role="img" aria-label="Glass office towers seen from below" style="background:linear-gradient(135deg,#24355a,#6f8fc0 50%,#1c2a45)"></div>
  <div class="body">
    <div class="date">Dec 12, 2023</div>
    <h4>Dorvant Legal joins Global Referral Network</h4>
    <p>Dorvant Legal is now a member of a leading global referral network — the largest legal referral network in the world — comprising 250 member firms located in more than 150 countries.</p>
    <a>Read More</a>
  </div>
</div>
<div class="abs news-item" style="top:4333px"><div class="media" role="img" aria-label="Judge gavel on a desk" style="background:linear-gradient(135deg,#e8e4df,#7a4a2c 55%,#3f5a4a)"></div><div class="body"><h5>Lorem Ipsum is<br>dummy text</h5><div class="date">Dec 12, 2023</div></div></div>
<div class="abs news-item" style="top:4466px"><div class="media" role="img" aria-label="Judge gavel on a desk" style="background:linear-gradient(135deg,#e8e4df,#7a4a2c 55%,#3f5a4a)"></div><div class="body"><h5>Lorem Ipsum is<br>dummy text</h5><div class="date">Dec 12, 2023</div></div></div>
<div class="abs news-item" style="top:4599px"><div class="media" role="img" aria-label="Judge gavel on a desk" style="background:linear-gradient(135deg,#e8e4df,#7a4a2c 55%,#3f5a4a)"></div><div class="body"><h5>Lorem Ipsum is<br>dummy text</h5><div class="date">Dec 12, 2023</div></div></div>

<!-- footer -->
<footer class="abs footer">
  <div class="abs" style="left:83px;top:108px;display:flex;align-items:center;gap:12px"><span class="brand-mark" style="background:#fff"></span><span class="brand-name" style="color:#fff">DORVANT LEGAL</span></div>
  <p class="abs" style="left:83px;top:178px;font-size:11px;line-height:15px;font-family:'PT Serif',serif">Lorem Ipsum is simply dummy text<br>of the typesetting industry.</p>
  <div class="abs" style="left:83px;top:270px;font-family:'PT Serif',serif;font-weight:700;font-size:15px">Folow Us On</div>
  <div class="abs" style="left:83px;top:302px;display:flex;gap:8px" aria-label="Social profiles">
    <span style="width:16px;height:16px;border-radius:50%;background:#fff"></span><span style="width:16px;height:16px;border-radius:50%;background:#fff"></span><span style="width:16px;height:16px;border-radius:50%;background:#fff"></span>
  </div>
  <div class="abs f-col" style="left:433px;top:90px"><h6>Quick Link</h6><ul><li>Pratice Areas</li><li>About</li><li>News</li><li>Resources</li><li>Contact Us</li></ul></div>
  <div class="abs f-col" style="left:608px;top:90px"><h6>Area of Practices</h6><ul><li>Business Litigation</li><li>Professional Negligence</li><li>Insurance Coverage</li></ul></div>
  <div class="abs f-col" style="left:871px;top:90px"><h6>Get In Touch</h6>
    <div class="f-contact"><svg width="14" height="18" viewBox="0 0 14 18"><path d="M7 0a7 7 0 0 0-7 7c0 5 7 11 7 11s7-6 7-11a7 7 0 0 0-7-7z" fill="#fff"/><circle cx="7" cy="7" r="2.5" fill="#0a3350"/></svg><span>48 Larchmere Street E, Ground<br>Floor Hamilton, ON L8N 0A4</span></div>
    <div class="f-contact"><svg width="14" height="14" viewBox="0 0 14 14"><path d="M3 1l2 3-1.5 1.5c1 2 3 4 5 5L10 9l3 2-1 2.5C6 13 1 8 .5 2z" fill="#fff"/></svg><span>+1 234-555-0188</span></div>
    <div class="f-contact"><svg width="14" height="12" viewBox="0 0 14 12"><rect x="1" y="1" width="12" height="10" fill="none" stroke="#fff" stroke-width="1.4"/><path d="M1 1l6 5 6-5" fill="none" stroke="#fff" stroke-width="1.4"/></svg><span>support@dorvantlegal.ca</span></div>
  </div>
  <div class="abs f-bottom" style="left:83px;top:436px">© 2023 Dorvant Legal. All Rights Reserved.</div>
  <div class="abs f-bottom" style="left:812px;top:438px;display:flex;gap:18px;font-size:10px"><span>Terms and Conditions</span><span>Privacy Policy</span><span>Disclaimer</span></div>
</footer>

</body>
</html>
```